Business Card Design

I need a business card design for a new company based in Sydney called 'The Copper Ladle'. We deliver organic, gourmet and fine foods to your door.

I would like to see creative, unique designs which use colours which represent health and nature like green.

Target Market(s)

Health conscious 20 to 35 year olds.

Industry/Entity Type

Health

Contact Information for Business Card

The Copper Ladle, Owen Barclett, owen@thecopperladle.com.au, 0427685392

Requirements
Must have
• My logo.

```html
<!DOCTYPE html>
<html lang="en">
<head>
<meta charset="UTF-8">
<title>The Copper Ladle – Business Card</title>
<link rel="stylesheet" href="https://fonts.googleapis.com/css2?family=Oswald:wght@700&display=swap">
<style>
  :root {
    --page: #ffffff;
    --card-light: #f4f8ec;
    --card-mid: #cfe29c;
    --card-deep: #abd157;
    --brand-green: #3f7f22;
    --mark-green: #8fbf2a;
    --ink: #2e2e2e;
  }
  html, body {
    margin: 0;
    padding: 0;
    width: 1200px;
    height: 700px;
    overflow: hidden;
    background: var(--page);
  }
  .canvas {
    position: relative;
    width: 1200px;
    height: 700px;
  }
  .business-card {
    position: absolute;
    left: 20px;
    top: 139px;
    width: 824px;
    height: 506px;
    background: linear-gradient(90deg, var(--card-light) 0%, var(--card-mid) 35%, var(--card-mid) 60%, var(--card-deep) 100%);
    overflow: hidden;
  }
  .brand-lockup {
    position: absolute;
    left: 62px;
    top: 60px;
    width: 140px;
    height: 420px;
  }
  .brand-name {
    position: absolute;
    left: 0;
    top: 0;
    transform-origin: left top;
    transform: translate(28px, 258px) rotate(-90deg);
    margin: 0;
    font-family: "Oswald", sans-serif;
    font-weight: 700;
    font-size: 40px;
    line-height: 1;
    letter-spacing: 1px;
    color: var(--brand-green);
    white-space: nowrap;
  }
  .brand-dot {
    position: absolute;
    left: 34px;
    top: 300px;
    width: 82px;
    height: 82px;
    border-radius: 50%;
    background: var(--mark-green);
  }
  .brand-emblem {
    position: absolute;
    left: 378px;
    top: 90px;
    width: 240px;
    height: 240px;
    border-radius: 50%;
    background: var(--mark-green);
  }
  .contact-block {
    position: absolute;
    left: 401px;
    top: 346px;
    margin: 0;
    font-family: "Oswald", sans-serif;
    font-weight: 700;
    font-size: 29px;
    line-height: 42px;
    color: var(--ink);
    letter-spacing: 0.3px;
  }
  .contact-block span { display: block; white-space: nowrap; }
</style>
</head>
<body>
<div class="canvas">
  <section class="business-card">
    <div class="brand-lockup">
      <p class="brand-name">The Copper Ladle</p>
      <div class="brand-dot" aria-hidden="true"></div>
    </div>
    <div class="brand-emblem" aria-hidden="true"></div>
    <p class="contact-block">
      <span>The Copper Ladle, Owen</span>
      <span>Barclett,</span>
      <span>owen@thecopperladle.com.au,</span>
      <span>0427685392</span>
    </p>
  </section>
</div>
</body>
</html>
```